Brightmend Outdoor Signage

We need an outdoor signage design for my company with new logo designed from artflockhub. We do electrical, Air conditioning & Plumbing, installation, service, repairs and maintenance. The design shall be an eye catching that cannot miss ready it.

Industry/Entity Type

Electrical, Air conditioning, Plumbing

```html
<!DOCTYPE html>
<html lang="en">
<head>
<meta charset="utf-8">
<title>Brightmend Outdoor Signage</title>
<link href="https://fonts.googleapis.com/css2?family=Montserrat:wght@700;800;900&family=Fira+Sans:wght@700&display=swap" rel="stylesheet">
<style>
  :root {
    --backdrop: #4a4948;
    --white: #ffffff;
    --orange: #f28a40;
    --blue: #156bb0;
    --navy: #1f437f;
    --red: #e62228;
  }
  * { margin: 0; padding: 0; box-sizing: border-box; }
  html, body { width: 1200px; height: 714px; overflow: hidden; background: var(--backdrop); }
  .canvas { position: relative; width: 1200px; height: 714px; }
  .sign {
    position: absolute; left: 20px; top: 67px; width: 1160px; height: 580px;
    background: var(--white); overflow: hidden;
    font-family: "Montserrat", sans-serif;
  }
  .sign-bands { position: absolute; inset: 0; width: 100%; height: 100%; }
  .brand { position: absolute; left: 62px; top: 200px; display: flex; align-items: center; gap: 16px; }
  .brand-dot { width: 66px; height: 66px; border-radius: 50%; background: var(--blue); }
  .brand-name { font-weight: 700; font-size: 86px; line-height: 1; color: var(--orange); letter-spacing: -1px; }
  .tagline {
    position: absolute; left: 80px; top: 385px;
    font-family: "Fira Sans", sans-serif; font-weight: 700; font-size: 29px; white-space: nowrap;
  }
  .tagline span { margin-right: 18px; }
  .tag-electrical { color: var(--red); }
  .tag-air { color: var(--blue); }
  .tag-plumbing { color: var(--orange); }
  .contact-icon { position: absolute; width: 46px; height: 46px; }
  .phone-icon { left: 726px; top: 84px; }
  .web-icon { left: 727px; top: 149px; }
  .phone-number {
    position: absolute; left: 787px; top: 78px;
    font-weight: 800; font-size: 50px; color: var(--blue); letter-spacing: 1px; line-height: 1.1;
  }
  .contact-lines {
    position: absolute; left: 794px; top: 145px;
    font-weight: 700; font-size: 17px; line-height: 26px; color: var(--blue);
  }
  .services { position: absolute; left: 780px; top: 330px; width: 340px; color: var(--white); }
  .service { position: relative; padding-left: 48px; }
  .service-icon { position: absolute; left: 0; top: 4px; width: 38px; height: 38px; }
  .service-name { font-weight: 800; font-size: 37px; line-height: 1; letter-spacing: 0.5px; }
  .service-rule {
    height: 3px; margin: 10px 0 14px 48px;
    background: linear-gradient(90deg, var(--white) 60%, rgba(255,255,255,0));
  }
</style>
</head>
<body>
<div class="canvas">
  <div class="sign">
    <svg class="sign-bands" viewBox="0 0 2060 1030" preserveAspectRatio="none" aria-hidden="true">
      <path fill="var(--orange)" d="M0 855 L890 855 C1000 855 1060 805 1095 765 C1165 690 1230 590 1290 540 C1350 490 1400 475 1470 475 L2060 475 L2060 1030 L0 1030 Z"/>
      <path fill="var(--navy)" d="M0 905 L920 905 C1030 905 1100 862 1150 800 C1210 720 1270 620 1320 580 C1370 535 1420 520 1470 520 L2060 520 L2060 1030 L0 1030 Z"/>
      <path fill="var(--blue)" d="M0 918 L920 918 C1035 918 1108 872 1160 808 C1220 728 1278 630 1328 592 C1378 548 1425 535 1470 535 L2060 535 L2060 1030 L0 1030 Z"/>
    </svg>

    <div class="brand">
      <div class="brand-dot"></div>
      <div class="brand-name">Brightmend</div>
    </div>
    <div class="tagline">
      <span class="tag-electrical">Electrical</span><span class="tag-air">Air Conditioning</span><span class="tag-plumbing">Plumbing</span>
    </div>

    <svg class="contact-icon phone-icon" viewBox="0 0 46 46" aria-hidden="true">
      <circle cx="23" cy="23" r="23" fill="var(--red)"/>
      <path d="M15 13 l5 -1 3 7 -3 2 c1 3 4 6 7 7 l2 -3 7 3 -1 5 c-10 1 -21 -10 -20 -20 z" fill="none" stroke="var(--white)" stroke-width="2.2" stroke-linejoin="round"/>
      <path d="M26 13 a8 8 0 0 1 7 7 M26 17 a4 4 0 0 1 3 3" fill="none" stroke="var(--white)" stroke-width="2" stroke-linecap="round"/>
    </svg>
    <div class="phone-number">0491 570 310</div>

    <svg class="contact-icon web-icon" viewBox="0 0 46 46" aria-hidden="true">
      <circle cx="23" cy="23" r="23" fill="var(--red)"/>
      <g fill="none" stroke="var(--white)" stroke-width="2.4">
        <circle cx="23" cy="23" r="12"/>
        <ellipse cx="23" cy="23" rx="5" ry="12"/>
        <path d="M11 23 H35 M23 11 V35"/>
      </g>
    </svg>
    <div class="contact-lines">
      <div>info@brightmendelectrical.com.au</div>
      <div>www.brightmendelectrical.com.au</div>
    </div>

    <div class="services">
      <div class="service">
        <svg class="service-icon" viewBox="0 0 38 38" aria-hidden="true">
          <circle cx="17" cy="17" r="11" fill="none" stroke="var(--white)" stroke-width="5" stroke-dasharray="4 3"/>
          <circle cx="17" cy="17" r="7" fill="none" stroke="var(--white)" stroke-width="3"/>
          <path d="M20 20 L34 34" stroke="var(--white)" stroke-width="4" stroke-linecap="round"/>
        </svg>
        <div class="service-name">INSTALLATION</div>
      </div>
      <div class="service-rule"></div>
      <div class="service">
        <svg class="service-icon" viewBox="0 0 38 38" aria-hidden="true">
          <path d="M19 1 l1.5 3.5 3.5 .3 -2.7 2.3 .9 3.5 -3.2 -2 -3.2 2 .9 -3.5 -2.7 -2.3 3.5 -.3 z" fill="var(--white)"/>
          <rect x="4" y="20" width="6" height="14" fill="var(--white)"/>
          <path d="M12 21 L17 14 C19 12 21 13 20 16 L19 19 H29 C31 19 31 23 29 23 C31 23 31 27 29 27 C31 27 30 31 28 31 C29 32 28 34 26 34 H12 Z" fill="var(--white)"/>
        </svg>
        <div class="service-name">SERVICE</div>
      </div>
      <div class="service-rule"></div>
      <div class="service">
        <svg class="service-icon" viewBox="0 0 38 38" aria-hidden="true">
          <path d="M6 4 a7 7 0 0 0 4 11 L28 33 a3 3 0 0 0 4 -4 L14 11 a7 7 0 0 0 -11 -4 l5 5 -2 2 -5 -5" fill="var(--white)"/>
        </svg>
        <div class="service-name">REPAIRS AND<br>MAINTENANCE</div>
      </div>
    </div>
  </div>
</div>
</body>
</html>
```